Wine Importer Needs a Wordpress Template

Our company, Corbanne Cellar Traders Ltd, requires a Wordpress template for our new website location (brastellcask.ie).

We specialise in importing Moldovan wine into Ireland. I have attached a presentation that has background information about the main winery and its wine. I would very much like to see something similar to this in feel and colour. I have also attached our logo which might be useful.

We are very much open to new ideas, so long as the result is something that is clean and easy to use.

Many thanks.
Updates

Project Deadline Extended
Reason: I have extended the deadline by a few days given that I was unable to respond timely to queries. My apologies to all for this. I will be available from now until the new deadline.

Project Deadline Extended

Industry/Entity Type

It Company

```html
<!DOCTYPE html>
<html lang="en">
<head>
<meta charset="utf-8">
<title>Corbanne Cellar Traders Ltd</title>
<link rel="stylesheet" href="https://fonts.googleapis.com/css2?family=Raleway:wght@400;500;600&family=Open+Sans:wght@400;600;700&family=Kaushan+Script&display=swap">
<style>
:root{
  --green:#2f8057;
  --green-dark:#246646;
  --green-line:#8fb59c;
  --wine:#7c1622;
  --ink:#2b2b2b;
  --body:#6a6a6a;
  --panel:#f4f4f4;
  --rule:#dedede;
  --white:#ffffff;
}
*{box-sizing:border-box;margin:0;padding:0}
html,body{width:1200px;height:2562px;overflow:hidden;background:var(--white)}
body{position:relative;font-family:"Open Sans",Arial,sans-serif;color:var(--body)}

/* navigation */
.site-nav{position:absolute;left:0;top:0;width:1200px;height:79px;background:var(--white);border-bottom:5px solid var(--green-line);z-index:3}
.nav-link{position:absolute;top:44px;font:600 15px "Open Sans",sans-serif;color:#333;letter-spacing:.3px;text-transform:uppercase}
.brand{position:absolute;left:546px;top:-2px;width:108px;height:108px;border-radius:50%;background:var(--white);border:3px solid var(--green);z-index:4;display:flex;align-items:center;justify-content:center;text-align:center}
.brand-name{font:600 11px/1.3 "Raleway",sans-serif;color:var(--green);text-transform:uppercase;letter-spacing:.5px;width:84px}

/* hero */
.hero{position:absolute;left:0;top:79px;width:1200px;height:587px;overflow:hidden}
.hero-photo{position:absolute;inset:0;background:
  radial-gradient(ellipse 140px 230px at 580px 360px, rgba(70,40,30,.45), transparent 75%),
  radial-gradient(ellipse 260px 200px at 120px 440px, rgba(190,180,60,.45), transparent 75%),
  radial-gradient(ellipse 260px 200px at 1080px 440px, rgba(190,180,60,.45), transparent 75%),
  linear-gradient(180deg,#a9b7a1 0%,#b8c09c 10%,#7f9550 26%,#5f7d2e 50%,#6f8a2a 75%,#4a5c1e 100%)}
.hero-shelf{position:absolute;left:0;bottom:0;width:1200px;height:44px;background:linear-gradient(180deg,#4c2a16,#2d180c)}
.hero-script{position:absolute;left:145px;top:142px;font:400 52px "Kaushan Script",cursive;color:var(--white)}
.hero-title{position:absolute;top:188px;font:500 66px "Raleway",sans-serif;color:var(--white)}
.dots{position:absolute;left:582px;top:574px;display:flex;gap:6px}
.dot{width:8px;height:8px;border-radius:50%;background:#cfcfcf}
.dot.on{background:var(--white)}

/* welcome */
.welcome-title{position:absolute;left:141px;top:716px;font:500 26px "Raleway",sans-serif;color:var(--ink)}
.welcome-title span{color:var(--green);font-weight:600}
.copy{font-size:13px;line-height:19px;color:var(--body)}
.copy p+p{margin-top:19px}
.welcome-copy{position:absolute;left:141px;top:756px;width:650px}
.welcome-photo{position:absolute;left:855px;top:670px;width:205px;height:325px;border-radius:8px;background:linear-gradient(180deg,#f3eded 0%,#6a2a32 30%,#3a2a26 65%,#6d7d3a 85%,#f3f0ea 100%)}

/* story timeline */
.story{position:absolute;left:0;top:1031px;width:1200px;height:859px;background:var(--panel);border-top:1px solid var(--rule);border-bottom:1px solid var(--rule)}
.story-axis{position:absolute;left:599px;top:0;width:1px;height:859px;background:var(--rule)}
.story-title{position:absolute;font:500 24px "Raleway",sans-serif;color:var(--ink)}
.story-copy{position:absolute;width:404px}
.story-photo{position:absolute;width:408px;height:200px}
.badge{position:absolute;left:564px;width:72px;height:72px;border-radius:50%;background:var(--green);color:var(--white);font:600 12px/15px "Open Sans",sans-serif;text-align:center;display:flex;align-items:center;justify-content:center}
.badge svg{position:absolute;top:28px}
.badge.tail-left svg{left:-14px}
.badge.tail-right svg{right:-14px}

/* featured */
.featured-title{position:absolute;left:141px;top:1932px;font:600 24px "Raleway",sans-serif;color:var(--ink)}
.carousel-arrows{position:absolute;left:1012px;top:1934px}
.product{position:absolute;top:2007px;width:175px;height:303px;background:var(--white);border:1px solid #e6e6e6;box-shadow:0 2px 8px rgba(0,0,0,.07);text-align:center}
.product-photo{position:absolute;left:64px;top:18px;width:46px;height:218px;border-radius:14px 14px 5px 5px}
.product-name{position:absolute;left:0;right:0;top:254px;font-size:14px;color:#444}
.product-grape{position:absolute;left:0;right:0;top:276px;font:700 14px "Open Sans",sans-serif;color:#222}
.tag{position:absolute;right:-16px;top:-16px;width:50px;height:50px;border-radius:50%;background:var(--wine);color:var(--white);font:700 11px/50px "Open Sans",sans-serif}

/* signup */
.signup{position:absolute;left:0;top:2381px;width:1200px;height:89px;background:var(--green)}
.signup-label{position:absolute;left:141px;top:29px;font:400 23px "Raleway",sans-serif;color:var(--white);white-space:nowrap}
.signup-input{position:absolute;left:610px;top:25px;width:308px;height:39px;background:var(--white);font:13px "Open Sans",sans-serif;color:#aaa;padding-left:12px;line-height:39px}
.signup-button{position:absolute;left:931px;top:25px;width:128px;height:39px;background:var(--green-dark);color:var(--white);font:600 12px/39px "Open Sans",sans-serif;text-transform:uppercase;padding-left:38px}
.signup-button svg{position:absolute;left:12px;top:12px}

/* footer */
.footer-copy{position:absolute;left:141px;top:2488px;font-size:12px;color:#444;line-height:24px}
.touch{position:absolute;left:910px;top:2488px;font-size:12px;color:#444}
.social{position:absolute;top:2514px;width:30px;height:30px;border-radius:50%}
</style>
</head>
<body>

<header class="site-nav">
  <a class="nav-link" style="left:228px">Home</a>
  <a class="nav-link" style="left:306px">About Us</a>
  <a class="nav-link" style="left:416px">Products</a>
  <a class="nav-link" style="left:700px">News</a>
  <a class="nav-link" style="left:781px">Gallery</a>
  <a class="nav-link" style="left:882px">Contact Us</a>
</header>
<div class="brand"><span class="brand-name">Corbanne Cellar Traders</span></div>

<section class="hero">
  <div class="hero-photo" role="img" aria-label="Vineyard hills with a bottle of white wine, a bottle of red wine and a glass of white wine on a wooden shelf"></div>
  <div class="hero-shelf"></div>
  <div class="hero-script">Rose dry wine</div>
  <div class="hero-title" style="left:228px">The Best</div>
  <div class="hero-title" style="left:662px">New Wine</div>
  <div class="dots"><span class="dot on"></span><span class="dot"></span><span class="dot"></span><span class="dot"></span></div>
</section>

<section class="welcome">
  <h1 class="welcome-title">Welcome to <span>Corbanne Cellar Traders Ltd.</span></h1>
  <div class="welcome-copy copy">
    <p>Lorem ipsum dolor sit amet, consectetur adipisicing elit, sed do eiusmod tempor incididunt ut labore et dolore magna aliqua. Ut enim ad minim veniam, quis nostrud exercitation ullamco laboris nisi ut aliquip ex ea commodo consequat.</p>
    <p>Duis aute irure dolor in reprehenderit in voluptate velit esse cillum dolore eu fugiat nulla pariatur. Excepteur sint occaecat cupidatat non proident, sunt in culpa qui officia deserunt mollit anim id est laborum.</p>
    <p>Lorem ipsum dolor sit amet, consectetur adipisicing elit, sed do eiusmod tempor incididunt ut labore et dolore magna aliqua. Ut enim ad minim veniam, quis nostrud exercitation ullamco laboris nisi ut aliquip ex ea commodo consequat.</p>
  </div>
  <div class="welcome-photo" role="img" aria-label="Bottle of red wine beside a filled glass and a bunch of grapes"></div>
</section>

<section class="story">
  <div class="story-axis"></div>

  <h2 class="story-title" style="left:141px;top:74px">Indignation translation H. Brandel</h2>
  <div class="story-copy copy" style="left:141px;top:114px">
    <p>Sed ut perspiciatis unde omnis iste natus error sit voluptatem accusantium doloremque laudantium, totam rem aperiam, eaque ipsa quae ab illo inventore veritatis et quasi architecto beatae vitae dicta sunt explicabo.</p>
    <p>Nemo enim ipsam voluptatem quia voluptas sit aspernatur aut odit aut fugit, sed quia consequuntur magni dolores eos qui ratione voluptatem sequi nesciunt.</p>
  </div>
  <div class="badge tail-right" style="top:58px"><svg width="16" height="16" viewBox="0 0 16 16"><path d="M0 0 L16 8 L0 16Z" fill="#2f8057"/></svg>Founded<br>1827</div>
  <div class="story-photo" role="img" aria-label="Sunlight over rows of a green vineyard" style="left:651px;top:79px;background:radial-gradient(circle at 22% 30%,#fff6c4,#e6b748 22%,#8aa33a 55%,#3f6a22 100%)"></div>

  <div class="story-photo" role="img" aria-label="Team celebrating with a trophy" style="left:141px;top:335px;background:linear-gradient(180deg,#7d95c4,#5f79ad 55%,#3e4f78)"></div>
  <div class="badge tail-left" style="top:346px"><svg width="16" height="16" viewBox="0 0 16 16"><path d="M16 0 L0 8 L16 16Z" fill="#2f8057"/></svg>Awards<br>1989</div>
  <h2 class="story-title" style="left:653px;top:346px">Awards 1989 Finibus Bonorum</h2>
  <div class="story-copy copy" style="left:653px;top:386px">
    <p>At vero eos et accusamus et iusto odio dignissimos ducimus qui blanditiis praesentium voluptatum deleniti atque corrupti quos dolores et quas molestias excepturi sint occaecati cupiditate non provident,</p>
    <p>similique sunt in culpa qui officia deserunt mollitia animi, id est laborum et dolorum fuga. Et harum quidem rerum facilis est et expedita distinctio.</p>
  </div>

  <h2 class="story-title" style="left:141px;top:606px">Awards 2012-2013 &nbsp;Finibus</h2>
  <div class="story-copy copy" style="left:141px;top:646px">
    <p>At vero eos et accusamus et iusto odio dignissimos ducimus qui blanditiis praesentium voluptatum deleniti atque corrupti quos dolores et quas molestias excepturi sint occaecati cupiditate non provident,</p>
    <p>similique sunt in culpa qui officia deserunt mollitia animi, id est laborum et dolorum fuga. Et harum quidem rerum facilis est et expedita distinctio.</p>
  </div>
  <div class="badge tail-right" style="top:609px"><svg width="16" height="16" viewBox="0 0 16 16"><path d="M0 0 L16 8 L0 16Z" fill="#2f8057"/></svg>Awards<br>2012-2013</div>
  <div class="story-photo" role="img" aria-label="Three people in suits holding trophies" style="left:651px;top:596px;background:linear-gradient(180deg,#a9c1e4,#8aa6d4 45%,#4a5060 70%,#1f232b)"></div>
</section>

<section class="featured">
  <h2 class="featured-title">Featured Product</h2>
  <svg class="carousel-arrows" width="46" height="30" viewBox="0 0 46 30"><path d="M14 4 L4 15 L14 26" fill="none" stroke="#c9c9c9" stroke-width="2"/><path d="M32 4 L42 15 L32 26" fill="none" stroke="#c9c9c9" stroke-width="2"/></svg>

  <div class="product" style="left:141px">
    <div class="product-photo" role="img" aria-label="Bottle of sparkling wine" style="background:linear-gradient(90deg,#0f2a1c,#2f5a40 45%,#0f2a1c)"></div>
    <div class="product-name">Aged red dry wine</div><div class="product-grape">100% Merlot</div>
    <div class="tag">NEW</div>
  </div>
  <div class="product" style="left:386px">
    <div class="product-photo" role="img" aria-label="Bottle of white wine" style="background:linear-gradient(90deg,#8e9a2a,#d9dc7a 45%,#8e9a2a)"></div>
    <div class="product-name">Yellow dry Wine</div><div class="product-grape">100% Merlot</div>
    <div class="tag">BEST</div>
  </div>
  <div class="product" style="left:638px">
    <div class="product-photo" role="img" aria-label="Bottle of dark red wine" style="background:linear-gradient(90deg,#111,#3a3a3a 45%,#111)"></div>
    <div class="product-name">Black dry Wine</div><div class="product-grape">100% Merlot</div>
    <div class="tag">NEW</div>
  </div>
  <div class="product" style="left:884px">
    <div class="product-photo" role="img" aria-label="Bottle of red wine" style="background:linear-gradient(90deg,#2a0a0e,#6a1a24 45%,#2a0a0e)"></div>
    <div class="product-name">Aldermoor Wine</div><div class="product-grape">100% Merlot</div>
    <div class="tag">BEST</div>
  </div>
</section>

<section class="signup">
  <div class="signup-label">Sign up for upcoming annoucements!</div>
  <div class="signup-input">Enter your email</div>
  <div class="signup-button"><svg width="18" height="14" viewBox="0 0 18 14"><rect x="0.5" y="0.5" width="17" height="13" fill="#fff"/><path d="M1 1 L9 8 L17 1" fill="none" stroke="#246646" stroke-width="1.5"/></svg>Subscribe</div>
</section>

<footer>
  <div class="footer-copy">© 2014 Corbanne Cellar Traders Ltd . All rights reserved.<br>Privacy Policy &nbsp;|&nbsp; Terms &amp; Conditions &nbsp;|&nbsp; Sitemap</div>
  <div class="touch">Be in touch</div>
  <span class="social" style="left:908px;background:#3b5998"></span>
  <span class="social" style="left:948px;background:#3a8fd6"></span>
  <span class="social" style="left:987px;background:#d14836"></span>
  <span class="social" style="left:1027px;background:#1d6fa8"></span>
</footer>

</body>
</html>
```